New Custom Pizza Box Design Project For Independant Restaurant

We are looking for creative designs for our new custom printed pizza boxes. Designs should include the following:

-Our logo & company name
-A color scheme similar to our current logo
-Our physical and URL addresses & phone number (menu is attached)
-Ability to scale the design across several box sizes (10x10x2, 14x14x2, 18x13x2,
26x18x2)
- Any creative flair you think will make for the best design

Design can be on a white or kraft (tan) box.
Designs can be either two or three ink colors.

***Please note, designs must be able to be screen printed on boxes***
Updates

Reason: Still debating which to choose

Target Market(s)

Industry/Entity Type

Pizza Delivery

Font styles to use
Other font styles liked:
• Please use font similar to our logo text

Requirements
Must have
• -2 or 3 ink colors
• -company name, address, phone number, URL
• -company logo and colors
• -flexibility to use on different box sizes (10x10x2, 14x14x2, 18x13x2,
• 26x18x2)
• -utilize full printable area on boxes (including 2" dimension on box sides)
• ***Please note, designs must be able to be screen printed on boxes***
Should not have
• Design features with strong similarities to existing designs of other pizzerias

```html
<!DOCTYPE html>
<html lang="en">
<head>
<meta charset="utf-8">
<title>Marco's Henhouse &amp; Pizzeria – Pizza Box Dieline</title>
<link rel="stylesheet" href="https://fonts.googleapis.com/css2?family=Oswald:wght@600&family=Ubuntu:wght@500;700&family=Arvo:wght@700&display=swap">
<style>
  :root {
    --paper: #ffffff;
    --panel-fill: #f6f5ef;
    --flap-fill: #e6e1cf;
    --flap-stripe: #cdbf98;
    --dieline: #e8274f;
    --brand-brown: #7a4a35;
    --brand-gold: #f2b51f;
    --brand-olive: #a89561;
  }
  * { margin: 0; padding: 0; box-sizing: border-box; }
  html, body {
    width: 1200px; height: 1000px; overflow: hidden;
    background: var(--paper);
  }
  .box-dieline { display: block; width: 1200px; height: 1000px; }
  .panel-texture { fill: var(--panel-fill); }
  .flap-texture { fill: var(--flap-fill); }
  .cut-line { fill: none; stroke: var(--dieline); stroke-width: 2; }
  .url-band { fill: var(--brand-brown); }
  .brand-name {
    font-family: "Oswald", sans-serif; font-weight: 600;
    fill: var(--brand-brown); text-anchor: middle; letter-spacing: 3px;
  }
  .brand-dot { fill: var(--brand-gold); }
  .phone {
    font-family: "Ubuntu", sans-serif; font-weight: 700;
    font-size: 28px; fill: var(--brand-gold);
  }
  .address {
    font-family: "Ubuntu", sans-serif; font-weight: 700;
    font-size: 13px; fill: var(--brand-olive); text-anchor: end;
  }
  .website {
    font-family: "Arvo", serif; font-weight: 700;
    font-size: 24px; fill: var(--brand-gold); text-anchor: middle; letter-spacing: 1px;
  }
</style>
</head>
<body>
<svg class="box-dieline" viewBox="0 0 1200 1000" xmlns="http://www.w3.org/2000/svg">
  <!-- side flaps -->
  <path class="flap-texture" role="img" aria-label="Tan brick wall texture on left side flap"
        d="M348 32 H420 V930 H378 L348 888 Z"/>
  <path class="flap-texture" role="img" aria-label="Tan brick wall texture on right side flap"
        d="M805 32 H858 V888 L830 930 H805 Z"/>

  <!-- lid and base panels -->
  <rect class="panel-texture" role="img" aria-label="Faint white brick wall texture on lid panel"
        x="420" y="52" width="385" height="430"/>
  <rect class="panel-texture" role="img" aria-label="Faint white brick wall texture on base panel"
        x="420" y="482" width="385" height="430"/>

  <!-- front tab with web address -->
  <path class="url-band" d="M408 912 H818 V950 L800 968 H426 L408 950 Z"/>
  <text class="website" x="613" y="943">marcoshenhouse.com</text>

  <!-- die cut and fold lines -->
  <g class="cut-line">
    <path d="M370 52 H846 V866 L830 886 V912 H420 V886 L370 886 Z"/>
    <line x1="370" y1="52" x2="370" y2="886"/>
    <line x1="370" y1="96" x2="846" y2="96"/>
    <line x1="370" y1="482" x2="846" y2="482"/>
    <line x1="420" y1="527" x2="805" y2="527"/>
    <line x1="420" y1="52" x2="420" y2="912"/>
    <line x1="805" y1="52" x2="805" y2="912"/>
    <line x1="370" y1="572" x2="420" y2="527"/>
    <line x1="846" y1="572" x2="805" y2="527"/>
    <line x1="420" y1="912" x2="420" y2="950"/>
    <path d="M420 950 L430 958 H796 L805 950 V912"/>
  </g>

  <!-- lid mark -->
  <circle class="brand-dot" cx="612" cy="290" r="34"/>

  <!-- brand lockup -->
  <g class="brand-lockup">
    <circle class="brand-dot" cx="612" cy="722" r="30"/>
    <text class="brand-name" x="612" y="628" font-size="40">MARCO'S</text>
    <text class="brand-name" x="612" y="680" font-size="46">HENHOUSE</text>
    <text class="brand-name" x="612" y="800" font-size="40">&amp; PIZZERIA</text>
  </g>

  <!-- contact details -->
  <text class="phone" x="440" y="894">555-0148</text>
  <text class="address" x="783" y="881">1427 Alder Street</text>
  <text class="address" x="783" y="897">Eastbrook Plaza</text>
</svg>
</body>
</html>
```